Company Web Design Project

Vantor grids works in the market of renewable energy with energy monitoring systems.

Vantor-grid wants a light and easy company website that informs about our core business and our products as well as the company. The sites should work on multiple platforms. It should include pictures and possibilities for news.
You find elements and company information on the following links:

http://vantor-grid.example/english-version/index.htm
some productinformation you find on this site:
http://kelwatch.example/

Vantor-grid AG is also interested in a Powerpoint template that matches the new website design as well as businesscards and a letter template.

Some more information about the company.

Headquartered in Karlsruhe, Germany, Vantor-Grid AG manufactures hardware & software solutions for remote monitoring, analysis, and control of electrical installations, alarm systems, and other critical networks.

In addition, our company provides test, measurement, and control equipment for use in a wide range of industrial and biological processes.

Founded in the year 2000, Vantor-Grid AG has established a comprehensive service network. Our solutions and systems are in operation e.g. in Europe, USA, Brazil, and Asia.

Vantor-Grid's team of experienced engineers, physicists, and network specialists continuously develop innovative solutions for many key industries - particularly in the renewable energies field.

To ensure the operational safety of their plants by means of optimized real time fault analysis routines

for process optimization

for a measurable increase in yield from production and trade.

Our products are distributed globally via an international dealer network.

In the interest of our customers and their needs, our aim is to expand this dealer network even more.
Updates

Target Market(s)

large solar project companies like, large renewable energy investors, large wholesellers for renewable energy, producer of solar panels.

Industry/Entity Type

Electrical

Requirements
Must have
• responsive design for multiple platforms

```html
<!DOCTYPE html>
<html lang="en">
<head>
<meta charset="utf-8">
<title>Vantor Grid – Interactive Technology</title>
<link rel="stylesheet" href="https://fonts.googleapis.com/css2?family=PT+Sans:ital,wght@0,400;0,700;1,400&family=PT+Sans+Narrow&display=swap">
<style>
:root{
  --teal:#0f8f79;
  --teal-dark:#0b7563;
  --nav:#5e6064;
  --text:#555;
  --muted:#6d6d6d;
  --light:#f1f1f1;
  --hero-dark:#3b3c3e;
  --news-bar:#b4b5b7;
}
*{margin:0;padding:0;box-sizing:border-box}
html,body{width:1151px;height:1200px;overflow:hidden;background:#fff}
body{font-family:"PT Sans",sans-serif;color:var(--text)}
.stage{position:relative;width:1400px;height:1460px;transform:scale(.8221);transform-origin:0 0}
.abs{position:absolute}
.topline{left:0;top:0;width:1400px;height:6px;background:var(--teal)}
.brand{left:212px;top:36px;display:flex;align-items:center;gap:10px}
.brand-mark{width:52px;height:52px;background:var(--teal)}
.brand-name{font-family:"PT Sans",sans-serif;font-weight:700;font-size:34px;color:#333;letter-spacing:-.5px}
.search{left:804px;top:62px;width:178px;height:24px;border:1px solid #ddd;font-size:9px;color:#999;padding:6px 9px}
.search svg{position:absolute;right:6px;top:4px}
.lang-label{left:1001px;top:70px;font-size:9px;color:#333}
.lang{left:1092px;top:62px;width:98px;height:24px;border:1px solid #ddd;font-size:12px;color:#333;display:flex;align-items:center;padding-left:8px;gap:8px}
.lang .flag{width:19px;height:12px;background:#2b3f8c}
.lang svg{margin-left:auto;margin-right:6px}
.nav{left:210px;top:126px;width:980px;display:flex;border-bottom:4px solid var(--teal);height:52px;background:var(--nav)}
.nav a{color:#fff;text-decoration:none;font-size:13px;display:flex;align-items:center;justify-content:center}
.nav a.active{background:var(--teal)}
.band{left:0;top:186px;width:1400px;height:382px;background:#ececec repeating-linear-gradient(45deg,#e4e4e4 0 1px,transparent 1px 3px)}
.hero-photo{left:210px;top:186px;width:655px;height:382px;background:linear-gradient(100deg,#6f7174,#b9babc 45%,#d9dadb 60%,#8a8b8d)}
.hero-panel{left:865px;top:186px;width:325px;height:382px;background:linear-gradient(180deg,#2f3032,#4a4b4d)}
.hero-title{left:896px;top:250px;width:280px;white-space:nowrap;font-family:"PT Sans Narrow",sans-serif;color:#fff;font-size:42px;line-height:1}
.hero-sub{left:896px;top:296px;width:280px;white-space:nowrap;font-family:"PT Sans Narrow",sans-serif;color:#fff;font-size:29px;line-height:34px}
.hero-text{left:896px;top:344px;width:270px;color:#fff;font-size:14px;line-height:22px}
.hero-btn{left:900px;top:475px;width:168px;height:34px;background:var(--teal);color:#fff;font-size:14px;display:flex;align-items:center;justify-content:center;gap:8px}
.dots{left:1115px;top:543px;display:flex;gap:3px}
.dots span{width:10px;height:10px;background:#8d8d8d}
.dots span:first-child{background:var(--teal)}
.side{left:210px;top:600px;width:240px;list-style:none}
.side li{height:34px;margin-bottom:4px;background:linear-gradient(#fff,#ececec);font-size:11px;color:#555;padding:0 15px;display:flex;align-items:center}
.side li.active{background:var(--teal);color:#fff;height:32px;margin-bottom:6px}
.welcome h1{font-weight:400;font-size:17px;color:var(--teal);margin-bottom:14px}
.welcome{left:478px;top:600px;width:712px}
.welcome p{font-size:11px;line-height:18px;color:var(--muted)}
.newsbar{left:478px;top:749px;width:712px;height:33px;background:var(--news-bar);color:#fff;font-size:16px;padding:0 13px;display:flex;align-items:center}
.newsbar .arrows{margin-left:auto;display:flex;gap:6px}
.news{top:804px;width:342px}
.news p{font-style:italic;font-size:11px;line-height:18px;color:var(--muted)}
.news time{display:block;font-size:11px;color:#333;margin-top:8px}
.btn-sm{display:inline-flex;align-items:center;justify-content:center;width:87px;height:24px;background:var(--teal);color:#fff;font-size:9px;margin-top:14px}
.divider{left:210px;top:958px;width:980px;height:1px;background:#ddd}
.products-title{left:210px;top:975px;width:980px;text-align:center;font-size:17px;color:var(--teal)}
.prod-arrows{left:1154px;top:981px;display:flex;gap:6px}
.card{top:1013px;width:231px}
.card .pic{height:101px}
.card .label{height:28px;background:var(--teal);color:#fff;font-size:11px;display:flex;align-items:center;padding-left:12px}
.card p{font-style:italic;font-size:11px;line-height:18px;color:var(--muted);margin-top:11px}
.footer{left:210px;top:1219px;width:980px;height:240px;background:var(--teal);color:#fff}
.fcol{position:absolute;top:22px}
.fcol h3{font-weight:400;font-size:14px;margin-bottom:6px}
.fcol ul{list-style:none;padding-left:2px}
.fcol li{font-size:9px;line-height:18px}
.frule{position:absolute;left:22px;top:177px;width:942px;height:1px;background:rgba(255,255,255,.25)}
.fbottom{position:absolute;left:27px;top:198px;font-size:9px;display:flex;gap:13px}
.social{position:absolute;left:748px;top:197px;display:flex;gap:22px}
.social span{width:16px;height:16px;border-radius:50%;background:rgba(255,255,255,.85)}
</style>
</head>
<body>
<div class="stage">
  <div class="abs topline"></div>

  <div class="abs brand"><span class="brand-mark"></span><span class="brand-name">vantor-grid</span></div>

  <div class="abs search">SEARCH :
    <svg width="16" height="16" viewBox="0 0 16 16"><circle cx="7" cy="7" r="5" fill="none" stroke="#ccc" stroke-width="1.5"/><line x1="11" y1="11" x2="15" y2="15" stroke="#ccc" stroke-width="1.5"/></svg>
  </div>
  <div class="abs lang-label">SELECT LANGUAGE :</div>
  <div class="abs lang"><span class="flag"></span>English
    <svg width="9" height="6" viewBox="0 0 9 6"><path d="M1 1l3.5 3.5L8 1" fill="none" stroke="#333" stroke-width="1.6"/></svg>
  </div>

  <nav class="abs nav">
    <a class="active" style="width:115px">HOME</a>
    <a style="width:130px">COMPANY</a>
    <a style="width:172px">BUSINESS AREAS</a>
    <a style="width:168px">PRODUCTS</a>
    <a style="width:162px">TOPICAL</a>
    <a style="width:68px">SERVICE</a>
    <a style="width:165px">CONTACT</a>
  </nav>

  <div class="abs band"></div>
  <div class="abs hero-photo" role="img" aria-label="Monochrome photo of a woman touching a digital interface with world map and menu overlays"></div>
  <div class="abs hero-panel"></div>
  <div class="abs hero-title">VANTOR GRID</div>
  <div class="abs hero-sub">INTERACTIVE TECHNOLOGY</div>
  <p class="abs hero-text">VANTOR-GRID AG MANUFACTURES HARDWARE &amp; SOFTWARE SOLUTIONS FOR REMOTE MONITORING, ANALYSIS, AND CONTROL OF ELECTRICAL INSTALLATIONS, ALARM SYSTEMS.</p>
  <div class="abs hero-btn">VIEW ALL DETAILS
    <svg width="14" height="10" viewBox="0 0 14 10"><path d="M1 1l4 4-4 4M8 1l4 4-4 4" fill="none" stroke="#fff" stroke-width="2"/></svg>
  </div>
  <div class="abs dots"><span></span><span></span><span></span><span></span><span></span></div>

  <ul class="abs side">
    <li class="active">YOUR NEAREST DEALER</li>
    <li>REGISTERING</li>
    <li>DOWNLOADS</li>
    <li>DATES</li>
    <li>PRESS RELEASES</li>
    <li>FAQ</li>
    <li>CONTACT FORM</li>
    <li>CONTACT PARTNERS</li>
    <li>EXTERNAL LINKS</li>
  </ul>

  <section class="abs welcome">
    <h1>WELCOME TO VANTOR GRID</h1>
    <p>For more than 10 years, Vantor-Grid's experts have been developing methods to increase the safety and efficiency of all types of energy plants. This is done by means of proven remote monitoring &amp; control systems, together with dedicated measurement and testing equipment. Primary activities: Reliable and efficient monitoring &amp; control of PV installations, biogas generating plants, and other regenerative energy sources, as well as monitoring systems for uninterruptible power supplies and other critical energy systems. For this, we develop hardware &amp; software solutions that can be integrated easily into our customers' existing installations. Without unnecessary installation work, and without additional software.</p>
  </section>

  <div class="abs newsbar">NEWS
    <span class="arrows">
      <svg width="8" height="12" viewBox="0 0 8 12"><path d="M6 1L2 6l4 5" fill="none" stroke="#fff" stroke-width="2"/></svg>
      <svg width="8" height="12" viewBox="0 0 8 12"><path d="M2 1l4 5-4 5" fill="none" stroke="#fff" stroke-width="2"/></svg>
    </span>
  </div>
  <article class="abs news" style="left:478px">
    <p>Die Steigerung der Endenergieeffizienz stellt die kostengünstigste und sinnvollste Brückentechnologie in ein regeneratives Stromzeitalter dar," dies ist eine der zentralen Erkenntnisse ...</p>
    <time>Donnerstag, 14.April 2011</time>
    <span class="btn-sm">READ MORE</span>
  </article>
  <article class="abs news" style="left:848px">
    <p>Die Steigerung der Endenergieeffizienz stellt die kostengünstigste und sinnvollste Brückentechnologie in ein regeneratives Stromzeitalter dar," dies ist eine der zentralen Erkenntnisse ...</p>
    <time>Donnerstag, 14.April 2011</time>
    <span class="btn-sm">READ MORE</span>
  </article>

  <div class="abs divider"></div>
  <h2 class="abs products-title" style="font-weight:400">OUR PRODUCTS</h2>
  <div class="abs prod-arrows">
    <svg width="8" height="12" viewBox="0 0 8 12"><path d="M6 1L2 6l4 5" fill="none" stroke="#bbb" stroke-width="2"/></svg>
    <svg width="8" height="12" viewBox="0 0 8 12"><path d="M2 1l4 5-4 5" fill="none" stroke="#bbb" stroke-width="2"/></svg>
  </div>

  <div class="abs card" style="left:210px">
    <div class="pic" role="img" aria-label="Close-up of orange and teal data logger hardware" style="background:linear-gradient(120deg,#3d8c8a,#e9874a 55%,#d9d4cc)"></div>
    <div class="label">DATA LOGGERS</div>
    <p>Data loggers from Vantor-Grid are based on three functional units ...</p>
  </div>
  <div class="abs card" style="left:460px">
    <div class="pic" role="img" aria-label="Finger touching glowing blue interface tiles" style="background:linear-gradient(120deg,#0d2f52,#2f7fb8 55%,#9cd0ee)"></div>
    <div class="label">APPLIANCES</div>
    <p>Nowadays, many companies and authorities place very high demands on their network security.</p>
  </div>
  <div class="abs card" style="left:710px">
    <div class="pic" role="img" aria-label="Business people in a meeting" style="background:linear-gradient(120deg,#c9d6e0,#8c9aa6 50%,#e4e6e8)"></div>
    <div class="label">SENSORS</div>
    <p>Data loggers from Vantor-Grid are based on three functional units ...</p>
  </div>
  <div class="abs card" style="left:959px">
    <div class="pic" role="img" aria-label="Businessman holding a glass globe" style="background:linear-gradient(120deg,#dfe6ec,#4a7ba8 45%,#1d1f22)"></div>
    <div class="label">DISPLAY SYSTEMS</div>
    <p>Data loggers from Vantor-Grid are based on three functional units ...</p>
  </div>

  <footer class="abs footer">
    <div class="fcol" style="left:30px"><h3>COMPANY</h3><ul><li>PROFILE</li><li>SERVICES</li><li>CONTACT PARTNERS</li><li>LOCATION|FIND US</li><li>JOBS</li></ul></div>
    <div class="fcol" style="left:220px"><h3>BUSINESS AREAS</h3><ul><li>SOLAR MONITORING</li><li>SAVING POTENTIALS</li><li>EV CHARGING POINTS</li><li>UPS MONITORING</li><li>BIOGAS POTENTIAL</li></ul></div>
    <div class="fcol" style="left:430px"><h3>PRODUCTS</h3><ul><li>DATALOGGER</li><li>APPLIANCES</li><li>SENSORS</li><li>DISPLAY SYSTEMS</li><li>SPECIAL SOLUTIONS</li></ul></div>
    <div class="fcol" style="left:620px"><h3>TOPICAL</h3><ul><li>NEWS</li><li>NEWS</li><li>ARCHIVE</li><li>PRESS RELEASES</li><li>PRESS REVIEW</li><li>DATES</li></ul></div>
    <div class="fcol" style="left:800px"><h3>SERVICE&amp;CONTACT</h3><ul><li>CONTACT FORM</li><li>DOWNLOADS</li><li>FAQ</li><li>TERMS &amp; CONDITIONS</li><li>LINKS</li></ul></div>
    <div class="frule"></div>
    <div class="fbottom"><span>COPYRIGHT 2013. VANTOR GRID. ALL RIGHTS RESERVED.</span><span>MASTHEAD</span><span>|</span><span>T&amp;CS</span><span>|</span><span>PRIVACY STATEMENT</span><span>|</span><span>JOBS</span></div>
    <div class="social"><span></span><span></span><span></span><span></span><span></span><span></span></div>
  </footer>
</div>
</body>
</html>
```